Harbor Stone Legal, PLLC
There are several individuals who are reviewing these designs.
velmoranti: #1 is very good - high on the list. #2 - no to the vertical business card, horizontal is better. #4 is unique - I don't think all parties have seen it. Like that creativity though.
@bluquartzpen - the blue/gold color combo is too harsh. The logo is unique, but again, to severe.
@moxelarts - the same as above: the blue/gold combo is too severe looking.
@tenorubi - we do not like the red with blue/white combo and there seems to be a lot going on there.
Thanks to all who are participating!I hope this feedback helps.
Could you provide feedback for the designs that have been submitted to this point? Thanks!
I not sue why this is saying its on hold because it shouldn't be. Please submit.
This company does not have a logo.
@Pardo - we do not have a logo! That's part of this whole design gig here, isn't it?
Please upload ai or eps file of your logo.

```html
<!DOCTYPE html>
<html lang="en">
<head>
<meta charset="utf-8">
<title>Harbor Stone Legal, PLLC – Business Card</title>
<link rel="stylesheet" href="https://fonts.googleapis.com/css2?family=EB+Garamond:wght@400;500&display=swap">
<style>
  :root {
    --page-bg: #e9eaec;
    --card-white: #ffffff;
    --brand-blue: #1f74b8;
    --brand-blue-deep: #1b66a3;
    --back-tint: #5aa4d8;
    --rule-grey: #b9bcc0;
    --text-grey: #7d8084;
    --text-white: #ffffff;
  }
  * { margin: 0; padding: 0; box-sizing: border-box; }
  html, body {
    width: 1200px; height: 1030px; overflow: hidden;
    background: var(--page-bg);
    font-family: "EB Garamond", Georgia, serif;
  }
  .sheet {
    position: relative; width: 1200px; height: 1030px;
  }
  .card {
    position: absolute; left: 250px; width: 700px; height: 400px;
    border-radius: 22px; overflow: hidden;
    box-shadow: 0 6px 20px rgba(0,0,0,0.18);
  }
  .card--front { top: 85px; background: var(--card-white); }
  .card--back  { top: 545px; background: var(--brand-blue); }

  .front__name {
    position: absolute; top: 30px; left: 0; width: 440px; text-align: center;
    color: var(--brand-blue); font-size: 34px; font-weight: 400;
  }
  .front__title {
    position: absolute; top: 74px; left: 0; width: 440px; text-align: center;
    color: var(--text-grey); font-size: 17px; letter-spacing: 0.5px;
  }
  .front__company {
    position: absolute; top: 150px; left: 70px;
    color: var(--brand-blue); font-size: 54px; font-weight: 400; white-space: nowrap;
  }
  .front__rule {
    position: absolute; top: 222px; left: 0; width: 100%; height: 6px;
    background: var(--rule-grey);
  }
  .front__band {
    position: absolute; top: 228px; left: 0; width: 100%; height: 172px;
    background: var(--brand-blue);
  }
  .contact {
    position: absolute; top: 245px; left: 70px;
    color: var(--text-white); font-size: 19px; line-height: 27px;
  }
  .back__company {
    position: absolute; top: 0; left: 0; width: 100%; height: 100%;
    display: flex; align-items: center; justify-content: center;
    color: var(--back-tint); font-size: 56px; font-weight: 400;
  }
</style>
</head>
<body>
<main class="sheet">
  <section class="card card--front" aria-label="Business card front">
    <div class="front__name">Daniel R. Ashcombe</div>
    <div class="front__title">Attorney at Law</div>
    <div class="front__company">Harbor Stone Legal, PLLC</div>
    <div class="front__rule"></div>
    <div class="front__band"></div>
    <address class="contact" style="font-style: normal;">
      418 Linden Crossing Ave Ashford, North Carolina 28190<br>
      Toll Free: English 704.310.5821 P: Spanish 704.310.5837<br>
      C: Vietnamese 704.310.5846 F: 704.310.5850<br>
      E: ashcombe@harborstonelegal.com harborstonelegal.com
    </address>
  </section>

  <section class="card card--back" aria-label="Business card back">
    <div class="back__company">Harbor Stone Legal, PLLC</div>
  </section>
</main>
</body>
</html>
```